11 x 11 Flyer Design for Social Media - Reverse Mortgages

62 or older?

A Reverse Mortgage
could be
Your Road to Financial Freedom

* No Monthly Payments
* No Income Requirements
* No Credit Score Requirements
* No Loss of Ownership

Receive cash by lump sum, monthly installments or a line of credit!!

Call us today for a Free Consultation!!
(800) 471-2965

Bluegate Financial Services, Inc.
NMLS #318760
www.bluegatehome.com

```html
<!DOCTYPE html>
<html lang="en">
<head>
<meta charset="utf-8">
<title>Reverse Mortgage Flyer – Bluegate Financial Services</title>
<link href="https://fonts.googleapis.com/css2?family=Lato:wght@400;700&family=Montserrat:wght@400;800&family=Oswald:wght@700&display=swap" rel="stylesheet">
<style>
  :root{
    --blue:#0b63ad;
    --blue-deep:#075aa2;
    --gold:#aa9a35;
    --gold-soft:#b6a440;
    --ink:#111;
    --white:#fff;
    --page:#f2f2f2;
  }
  *{margin:0;padding:0;box-sizing:border-box}
  html,body{width:1200px;height:1200px;overflow:hidden;background:var(--page)}
  .flyer{
    position:absolute;left:0;top:0;width:1237px;height:1237px;
    transform:scale(0.97009);transform-origin:0 0;
    background:var(--white);overflow:hidden;font-family:'Lato',sans-serif;
  }
  .backdrop{position:absolute;inset:0}
  .brand{
    position:absolute;left:690px;top:160px;
    font-family:'Lato',sans-serif;font-weight:700;font-size:22px;color:var(--blue);
    display:flex;align-items:center;gap:10px;white-space:nowrap;
  }
  .brand-dot{width:18px;height:18px;border-radius:50%;background:var(--blue);flex:none}
  .age-question{
    position:absolute;left:575px;top:292px;
    font-family:'Montserrat',sans-serif;font-weight:800;font-size:76px;letter-spacing:1px;
    color:var(--blue-deep);white-space:nowrap;
  }
  .age-question .accent{color:var(--gold)}
  .features{position:absolute;left:0;top:435px;width:463px;list-style:none}
  .feature{position:absolute;left:0;width:463px}
  .feature-icon{position:absolute;width:96px;height:96px}
  .feature-label{position:absolute;left:47px;color:var(--white);font-size:27px;white-space:nowrap}
  .headline{
    position:absolute;left:517px;top:640px;
    font-family:'Oswald',sans-serif;font-weight:700;font-size:52px;line-height:59px;
    transform:scaleX(0.86);transform-origin:0 0;white-space:nowrap;text-transform:uppercase;
  }
  .headline .line-gold{color:var(--gold);display:block;letter-spacing:1.8px}
  .headline .line-blue{color:var(--blue-deep);display:block}
  .payout-pill{
    position:absolute;left:517px;top:765px;width:647px;height:36px;border-radius:18px;
    background:var(--gold);color:var(--white);font-family:'Montserrat',sans-serif;font-size:17.5px;
    letter-spacing:.5px;line-height:36px;padding-left:9px;white-space:nowrap;
  }
  .about{
    position:absolute;left:522px;top:816px;width:665px;font-size:14.8px;line-height:18.8px;color:var(--ink);
  }
  .cta{
    position:absolute;left:625px;top:928px;color:var(--blue-deep);
    font-weight:700;font-size:36.5px;line-height:45px;letter-spacing:-.3px;
  }
  .phone{
    position:absolute;left:646px;top:1018px;display:flex;align-items:center;gap:22px;
    color:var(--gold);font-weight:700;font-size:47px;
  }
  .footer{
    position:absolute;left:0;top:1093px;width:1237px;height:144px;background:var(--gold-soft);
  }
  .footer-company{
    position:absolute;left:136px;top:40px;color:var(--white);font-weight:700;font-size:20px;line-height:27px;
  }
  .footer-divider{position:absolute;left:616px;top:20px;width:2px;height:82px;background:rgba(255,255,255,.85)}
  .footer-web{
    position:absolute;left:758px;top:50px;color:var(--white);font-weight:700;font-size:19px;letter-spacing:1.5px;
  }
</style>
</head>
<body>
<div class="flyer">
  <svg class="backdrop" width="1237" height="1237" viewBox="0 0 1237 1237">
    <defs>
      <linearGradient id="beachTone" x1="0" y1="0" x2="1" y2="0">
        <stop offset="0" stop-color="#c9d1d6"/>
        <stop offset="0.45" stop-color="#dfe4e6"/>
        <stop offset="0.75" stop-color="#ffffff"/>
      </linearGradient>
      <linearGradient id="waveTone" gradientUnits="userSpaceOnUse" x1="0" y1="200" x2="0" y2="1072">
        <stop offset="0" stop-color="#0f6cb8"/>
        <stop offset="1" stop-color="#075aa2"/>
      </linearGradient>
    </defs>
    <rect x="0" y="0" width="1237" height="620" fill="url(#beachTone)" role="img" aria-label="Photo of a smiling senior couple in white clothes on a beach"/>
    <path class="wave-gold" d="M0 165 C300 500 800 580 1237 368 L1237 503 C1000 600 700 620 463 575 L463 1032 Q463 1072 423 1072 L0 1072 Z" fill="var(--gold)"/>
    <path class="wave-blue" d="M0 185 C300 515 800 575 1237 368 L1237 478 C1000 572 700 596 463 552 L463 1032 Q463 1072 423 1072 L0 1072 Z" fill="url(#waveTone)"/>
  </svg>

  <div class="brand"><span class="brand-dot"></span>Bluegate Financial Services, Inc.</div>

  <div class="age-question">62 OR <span class="accent">OLDER ?</span></div>

  <ul class="features">
    <li class="feature" style="top:0">
      <svg class="feature-icon" style="left:137px;top:0" viewBox="0 0 96 96">
        <circle cx="48" cy="48" r="46" fill="none" stroke="#fff" stroke-width="2"/>
        <circle cx="48" cy="48" r="38" fill="#aa9a35"/>
        <path d="M30 42 A19 19 0 0 1 64 38" fill="none" stroke="#fff" stroke-width="3"/>
        <path d="M66 54 A19 19 0 0 1 32 58" fill="none" stroke="#fff" stroke-width="3"/>
        <text x="48" y="58" text-anchor="middle" font-family="Lato,sans-serif" font-weight="700" font-size="28" fill="#fff">$</text>
      </svg>
      <span class="feature-label" style="top:103px">No Monthly Payments</span>
    </li>
    <li class="feature" style="top:160px">
      <svg class="feature-icon" style="left:140px;top:0" viewBox="0 0 96 96">
        <circle cx="48" cy="48" r="46" fill="none" stroke="#fff" stroke-width="2"/>
        <circle cx="48" cy="48" r="38" fill="#aa9a35"/>
        <circle cx="42" cy="38" r="10" fill="#fff"/><circle cx="58" cy="26" r="7" fill="#fff"/>
        <path d="M24 60 Q36 54 48 60 L66 56 Q70 60 64 64 L44 72 L24 70 Z" fill="#fff"/>
      </svg>
      <span class="feature-label" style="top:102px">No Income Requirements</span>
    </li>
    <li class="feature" style="top:312px">
      <svg class="feature-icon" style="left:138px;top:0" viewBox="0 0 96 96">
        <circle cx="48" cy="48" r="46" fill="none" stroke="#fff" stroke-width="2"/>
        <circle cx="48" cy="48" r="38" fill="#aa9a35"/>
        <circle cx="48" cy="46" r="26" fill="none" stroke="#fff" stroke-width="2.5"/>
        <path d="M48 46 L62 32" stroke="#fff" stroke-width="3"/>
        <rect x="36" y="58" width="24" height="9" rx="4" fill="none" stroke="#fff" stroke-width="1.5"/>
      </svg>
      <span class="feature-label" style="top:102px">No Credit Score Requirements</span>
    </li>
    <li class="feature" style="top:458px">
      <svg class="feature-icon" style="left:138px;top:0" viewBox="0 0 96 96">
        <circle cx="48" cy="48" r="46" fill="none" stroke="#fff" stroke-width="2"/>
        <circle cx="48" cy="48" r="38" fill="#aa9a35"/>
        <circle cx="58" cy="38" r="11" fill="#fff"/>
        <path d="M52 46 L30 68 L34 72 L38 68 L42 72 L46 68 L42 64 L58 48 Z" fill="#fff"/>
      </svg>
      <span class="feature-label" style="top:108px">No Loss of Ownership</span>
    </li>
  </ul>

  <h1 class="headline">
    <span class="line-gold">A Reverse Mortgage Could Be</span>
    <span class="line-blue">Your Road to Financial Freedom</span>
  </h1>

  <div class="payout-pill">Receive cash by lump sum, monthly installments or a line of credit !!</div>

  <p class="about">Since 1997, we have served the MD, DC &amp; VA area by providing an array of mortgage loan products tailored to our clients unique needs and desires. Our responsibility to our local communities does not stop there. We also seek to provide members of our neighboring communities with tools, resources and the necessary counseling to make sound decisions not only relating to their real estate investments, but also their overall personal finances.</p>

  <p class="cta">CALL US TODAY FOR A<br>FREE CONSULTATION!!</p>

  <div class="phone">
    <svg width="38" height="38" viewBox="0 0 38 38" aria-hidden="true">
      <circle cx="19" cy="19" r="17" fill="none" stroke="#0b63ad" stroke-width="2.5"/>
      <path d="M13 10 L16 10 L17.5 14 L15.5 16 Q17 20.5 22 22.5 L24 20.5 L28 22 L28 25 Q26 28 22 27 Q13 24 11 15 Q10 11 13 10 Z" fill="#0b63ad"/>
    </svg>
    <span>(800) 471-2965</span>
  </div>

  <footer class="footer">
    <div class="footer-company">Bluegate Financial Services, Inc.<br>NMLS #318760</div>
    <div class="footer-divider"></div>
    <div class="footer-web">www.bluegatehome.com</div>
  </footer>
</div>
</body>
</html>
```